Pause Your Day And Browse- PYDB poster

I am the Vice President of Advocacy for the Coastline Shelfkeepers Guild. I am looking to have a set of posters made for PYDB (Pause Your Day and Browse) October 23. PYDB is a time when all school children in BC are encouraged to Pause Your Day and Browse for 15-20 minutes at some point in their day.

I would like to get a set of 2 digital posters designed (if possible it would be nice to have the option to print to both 11 x 17 and 8.5 x 11 paper). We need a poster that is high school (Grade 8-12) appropriate and one that is elementary (Grade k-7) appropriate. Both posters need to be replicated in French. All posters need to have the KWNU logo on them as well as the Coastline Shelfkeepers Guild Logo.

Here is a link to last year's successful design http://kwnu-example.org/csg/info/advocacy.html
There are two additional samples in the uploaded files section.

Each poster needs to have the following information:

-Pause Your Day and Browse (PYDB)
- The date Monday, October 23, 2017
-the logo for the KWNU (attached)
-the logo for the CSG (attached)- the logos do not have to be large.

Target Market(s)

Children ages 5-12 and 12-17 as well as their teachers

Industry/Entity Type

Teacher

Font styles to use
Sans Serif

Requirements
Must have
• Must have both logos- colours may be changed for either or both
Nice to have
• Clear, Bright lettering. Images of child or children enjoying reading
Should not have
• stereotypes

```html
<!DOCTYPE html>
<html lang="en">
<head>
<meta charset="utf-8">
<title>PYDB Poster Set</title>
<link rel="stylesheet" href="https://fonts.googleapis.com/css2?family=Montserrat:wght@700&family=Raleway:wght@400&family=Arvo:ital,wght@1,700&display=swap">
<style>
  :root {
    --board: #fddcc0;
    --board-glow: #fff4c4;
    --sky-top: #7d7686;
    --sky-mid: #b8918a;
    --sky-glow: #eda649;
    --ground: #1a140c;
    --white: #ffffff;
    --orange: #f5a526;
    --shadow: #3a2410;
  }
  * { box-sizing: border-box; margin: 0; padding: 0; }
  html, body { width: 1200px; height: 787px; overflow: hidden; }
  body {
    position: relative;
    background:
      linear-gradient(90deg, transparent 44%, var(--board-glow) 50%, transparent 56%),
      radial-gradient(ellipse at 50% 50%, var(--board-glow) 0%, transparent 30%),
      var(--board);
    font-family: "Raleway", sans-serif;
  }
  .poster {
    position: absolute;
    width: 575px;
    height: 372px;
    overflow: hidden;
  }
  .poster--tl { left: 15px;  top: 15px; }
  .poster--tr { left: 610px; top: 15px; }
  .poster--bl { left: 15px;  top: 402px; }
  .poster--br { left: 610px; top: 402px; }

  .poster__photo {
    position: absolute;
    inset: 0;
    background:
      linear-gradient(0deg, var(--ground) 0%, var(--ground) 9%, transparent 16%),
      linear-gradient(90deg, var(--ground) 0%, rgba(26,20,12,.85) 30%, rgba(26,20,12,.35) 52%, transparent 62%),
      linear-gradient(180deg, var(--sky-top) 0%, var(--sky-mid) 45%, var(--sky-glow) 82%, #f6c25c 90%);
  }
  .poster__title {
    position: absolute;
    left: 275px;
    top: 100px;
    width: 280px;
    text-align: center;
    line-height: 1;
    font-weight: 400;
  }
  .wordmark {
    display: block;
    font-size: 86px;
    text-shadow: 3px 3px 0 var(--shadow), 4px 5px 6px rgba(0,0,0,.45);
  }
  .wordmark--plain { font-family: "Montserrat", sans-serif; font-weight: 700; color: var(--white); }
  .wordmark--bold  { font-family: "Arvo", serif; font-style: italic; font-weight: 700; color: var(--orange); font-size: 80px; }
  .tagline {
    display: block;
    margin-top: 14px;
    font-family: "Raleway", sans-serif;
    font-weight: 400;
    font-size: 22px;
    line-height: 25px;
    color: var(--white);
    text-transform: uppercase;
    white-space: nowrap;
  }
  .poster__partners {
    position: absolute;
    right: 10px;
    bottom: 44px;
    display: flex;
    flex-direction: column;
    align-items: flex-end;
    gap: 6px;
  }
  .partner {
    display: flex;
    align-items: center;
    gap: 6px;
    font-family: "Montserrat", sans-serif;
    font-weight: 700;
    font-size: 14px;
    color: var(--white);
  }
  .partner__dot { width: 14px; height: 14px; border-radius: 50%; background: var(--white); }
  .poster__date {
    position: absolute;
    left: 0;
    width: 100%;
    bottom: 7px;
    padding-left: 90px;
    text-align: center;
    font-size: 16px;
    color: var(--white);
    letter-spacing: .3px;
  }
</style>
</head>
<body>

<section class="poster poster--tl">
  <div class="poster__photo" role="img" aria-label="Photo: silhouette of a child reading a book against a tree at sunset"></div>
  <h1 class="poster__title">
    <span class="wordmark wordmark--plain">PYDB</span>
    <span class="tagline">Pause Your Day<br>And Browse</span>
  </h1>
  <div class="poster__partners">
    <span class="partner"><span class="partner__dot"></span>KWNU</span>
    <span class="partner">CSG</span>
  </div>
  <p class="poster__date">Monday, October 23, 2017</p>
</section>

<section class="poster poster--tr">
  <div class="poster__photo" role="img" aria-label="Photo: silhouette of a child reading a book against a tree at sunset"></div>
  <h1 class="poster__title">
    <span class="wordmark wordmark--bold">PYDB</span>
    <span class="tagline">Pause Your Day<br>And Browse</span>
  </h1>
  <div class="poster__partners">
    <span class="partner"><span class="partner__dot"></span>KWNU</span>
    <span class="partner">CSG</span>
  </div>
  <p class="poster__date">Monday, October 23, 2017</p>
</section>

<section class="poster poster--bl" lang="fr">
  <div class="poster__photo" role="img" aria-label="Photo : silhouette d’un enfant lisant un livre contre un arbre au coucher du soleil"></div>
  <h1 class="poster__title">
    <span class="wordmark wordmark--bold">PYDB</span>
    <span class="tagline">Fais une pause<br>et feuillette</span>
  </h1>
  <div class="poster__partners">
    <span class="partner"><span class="partner__dot"></span>KWNU</span>
    <span class="partner">CSG</span>
  </div>
  <p class="poster__date" lang="en">Monday, October 23, 2017</p>
</section>

<section class="poster poster--br" lang="fr">
  <div class="poster__photo" role="img" aria-label="Photo : silhouette d’un enfant lisant un livre contre un arbre au coucher du soleil"></div>
  <h1 class="poster__title">
    <span class="wordmark wordmark--plain">PYDB</span>
    <span class="tagline">Fais une pause<br>et feuillette</span>
  </h1>
  <div class="poster__partners">
    <span class="partner"><span class="partner__dot"></span>KWNU</span>
    <span class="partner">CSG</span>
  </div>
  <p class="poster__date" lang="en">Monday, October 23, 2017</p>
</section>

</body>
</html>
```